Tarn Studio PPT design

We are looking for a fresh and funky PPT design that is both eye-catching and allows room/whitespace for us to get the content across. We are a social media agency based in China and our logo although simple sort of reflects the nature of the company. There are two main tasks for this PPT, one as a business card to show-case our case-studies, but also as a back-drop to our pitch presentations and other client presentations. These presentations are a mix of visuals, text and graphs. The key message we want to get across is that we are professional, creative and fresh. We think that using our four support colours may work but are open to suggestions.
Current website www.tarnasia-example.com
Reason: Hi All,
as we have just guaranteed the payment we extended the deadline to allow for more submissions. Please bear with us.
Thanks,
Tarn Studio Team
Reason: To see more designs, we extend the deadline to March 18, 2014. Thanks.
Target Market(s)
Marketing CMO's, company CEO's, product managers, social media managers
Industry/Entity Type
Business

```html
<!DOCTYPE html>
<html lang="en">
<head>
<meta charset="utf-8">
<title>Tarn Studio – Presentation Title Slide</title>
<link rel="stylesheet" href="https://fonts.googleapis.com/css2?family=Saira:wght@400;600;800&display=swap">
<style>
  :root {
    --page: #e6e6e4;
    --header: #1e202b;
    --footer: #0c0e18;
    --white: #ffffff;
    --lime: #84c634;
    --purple: #6a0f7a;
    --magenta: #e3037f;
    --orange: #e85d22;
    --ink: #0e1018;
  }
  * { box-sizing: border-box; margin: 0; padding: 0; }
  html, body {
    width: 1200px; height: 1000px; overflow: hidden;
    background: var(--page);
    font-family: "Saira", "Arial", sans-serif;
  }
  .slide {
    position: absolute; left: 0; top: 50px;
    width: 1200px; height: 900px;
    background: var(--lime);
    overflow: hidden;
  }
  .header {
    position: absolute; left: 0; top: 0;
    width: 1200px; height: 206px;
    background: var(--header);
  }
  .divider {
    position: absolute; left: 0; top: 206px;
    width: 1200px; height: 17px;
    background: var(--white);
  }
  .brand {
    position: absolute; left: 80px; top: 78px;
    display: flex; align-items: center; gap: 16px;
  }
  .brand-mark {
    width: 22px; height: 22px; background: var(--orange);
  }
  .brand-name {
    color: var(--white);
    font-weight: 800; font-size: 54px; line-height: 1;
    letter-spacing: -0.5px;
  }
  .colour-bar {
    position: absolute; top: 84px;
    width: 128px; height: 38px;
  }
  .colour-bar.lime { left: 501px; background: var(--lime); }
  .colour-bar.purple { left: 702px; background: var(--purple); }
  .colour-bar.magenta { left: 904px; background: var(--magenta); }
  .colour-bar.orange { left: 1072px; background: var(--orange); }
  .divider-dot {
    position: absolute; left: 565px; top: 183px;
    width: 70px; height: 70px;
  }
  .title-block {
    position: absolute; left: 0; top: 0; width: 1200px;
    text-align: center; color: var(--ink);
  }
  .title {
    position: absolute; left: 0; top: 398px; width: 1200px;
    font-weight: 800; font-size: 80px; line-height: 1;
    letter-spacing: 1px;
  }
  .subtitle {
    position: absolute; left: 0; top: 547px; width: 1200px;
    font-weight: 400; font-size: 54px; line-height: 1;
    letter-spacing: 1px;
  }
  .footer {
    position: absolute; left: 0; top: 865px;
    width: 1200px; height: 35px;
    background: var(--footer);
  }
  .web-tab {
    position: absolute; left: 385px; top: 838px;
    width: 430px; height: 62px;
    background: var(--footer);
    border-radius: 28px 28px 0 0;
    color: var(--white);
    font-size: 26px; font-weight: 400;
    text-align: center; line-height: 52px;
  }
</style>
</head>
<body>
  <main class="slide">
    <header class="header">
      <div class="brand">
        <span class="brand-mark"></span>
        <span class="brand-name">Tarn Studio</span>
      </div>
      <span class="colour-bar lime"></span>
      <span class="colour-bar purple"></span>
      <span class="colour-bar magenta"></span>
      <span class="colour-bar orange"></span>
    </header>
    <div class="divider"></div>
    <svg class="divider-dot" viewBox="0 0 70 70" aria-hidden="true">
      <circle cx="35" cy="35" r="35" fill="#ffffff"/>
      <circle cx="35" cy="35" r="22" fill="#e85d22"/>
    </svg>
    <section class="title-block">
      <h1 class="title">PRESENTATION TITLE</h1>
      <p class="subtitle">Presentation Subtitle</p>
    </section>
    <footer class="footer"></footer>
    <div class="web-tab">www.tarnasia-example.com</div>
  </main>
</body>
</html>
```